Stationery Design Project

Would like to have the design elements we created in for our website (www.brook-holdings.example), incorporated in a stationery design layout.
Updates
Colors used in the logo attachments do not need to be used. We are open to different color variations. Looking for a crisp, clean, modern update using the design elements in attachments and which can also be viewed on or website.
A note to designers:
Project Deadline Extended
Reason: Due to update in our project description and requirements, we have decided to extend the deadline of this project to provide ample opportunity to all designers participating .
Requirements
Must have
- Must have continuity with the theme and design features used in our website. Have attached .jpg images of some of the design elements.

```html
<!DOCTYPE html>
<html lang="en">
<head>
<meta charset="utf-8">
<title>Brook Holdings Letterhead</title>
<link rel="stylesheet" href="https://fonts.googleapis.com/css2?family=Source+Sans+3:wght@400;600&display=swap">
<style>
  :root {
    --paper: #ffffff;
    --forest-dark: #0f2a17;
    --forest: #1f5a2c;
    --leaf-green: #3bb54a;
    --contact-green: #3aa648;
    --brand-blue: #1d7fc2;
    --ink: #1c1c1c;
  }
  * { margin: 0; padding: 0; box-sizing: border-box; }
  html, body {
    width: 849px; height: 1200px; overflow: hidden;
    background: var(--paper);
  }
  .letterhead {
    position: relative;
    width: 849px; height: 1200px;
    background: var(--paper);
    font-family: "Source Sans 3", "Myriad Pro", Arial, sans-serif;
  }
  .header-swoosh {
    position: absolute; top: 0; left: 0;
    width: 849px; height: 260px;
  }
  .brand {
    position: absolute; top: 52px; left: 418px;
    display: flex; align-items: center; gap: 10px;
  }
  .brand-dot {
    width: 18px; height: 18px; border-radius: 50%;
    background: var(--leaf-green);
  }
  .brand-name {
    font-size: 52px; font-weight: 600; line-height: 1;
    color: var(--brand-blue);
    letter-spacing: 0.2px;
  }
  .contact {
    position: absolute; top: 158px; left: 432px;
    font-size: 23px; line-height: 31px;
    color: var(--contact-green);
    list-style: none;
  }
  .contact .fax { padding-left: 36px; }
  .contact .phone { padding-left: 8px; }
  .footer {
    position: absolute; left: 51px; right: 51px; top: 1131px;
    border-top: 1.5px solid var(--ink);
    text-align: center;
    padding-top: 6px;
    font-size: 21px;
    color: var(--ink);
  }
</style>
</head>
<body>
  <div class="letterhead">
    <svg class="header-swoosh" viewBox="0 0 849 260" aria-hidden="true">
      <defs>
        <linearGradient id="forestShade" x1="0" y1="0" x2="1" y2="1">
          <stop offset="0" stop-color="#1d5029"/>
          <stop offset="0.6" stop-color="#0f2a17"/>
          <stop offset="1" stop-color="#163d20"/>
        </linearGradient>
      </defs>
      <path class="swoosh-light" fill="#3bb54a"
        d="M0 0 H592 C470 20 300 70 200 120 C130 158 60 200 0 232 Z"/>
      <path class="swoosh-dark" fill="url(#forestShade)"
        d="M0 0 H592 C500 6 420 26 370 50 C320 72 280 100 250 118 C170 160 80 200 0 232 Z"/>
      <rect class="script-flourish" role="img" aria-label="Hand-lettered script flourish"
        x="14" y="8" width="340" height="120" rx="6" fill="#173f21" opacity="0.55"/>
    </svg>

    <div class="brand">
      <span class="brand-dot"></span>
      <span class="brand-name">Brook Holdings</span>
    </div>

    <ul class="contact">
      <li class="phone">Phone : (555) 014- 2290</li>
      <li class="fax">Fax&nbsp; : (555) 014-2291</li>
      <li class="email">E-mail : info@brook-holdings.example</li>
    </ul>

    <div class="footer">Brook Holdings, Inc. 418 Linden Weg Suite 120 Alder, GA 30999</div>
  </div>
</body>
</html>
```